The Willow Lantern Supper Club & Restaurant MENU RE-Design

I would like a professional layed out menu re-type.. Black background preferred with white letters.. but open to ideas.. I have attached our current menu which we believe is not layed out correctly and we would like to have the RAW ie shrimp, cocktail. chilled lobster tail, oysters and tuna wontons perhaps in a box or something listed first.. Re-organized menu items.. but would like Apps, housemade flatbreads and the main subject discriptions listed as in our current menu. Help us enhance our menu.. not looking for pictures.. just clean and modern.. thanks! Please also NOTE.. We have our logo on the front cover of black leather menu jackets all 6 pages are inserted via corner tabs.. Everything needs to fit on 6-
8.5 x 11 pages...

Industry/Entity Type

Restaurant

Requirements
Must have
• 6 Total Pages on 8.5 x 11 sized paper potrait.
• also entire menu items on the page as there are lots of items.. just submiting few menu items doesnt give us a look at how the entire menu will read
Nice to have
• EASY TO READ with dim lighting..

```html
<!DOCTYPE html>
<html lang="en">
<head>
<meta charset="utf-8">
<title>The Willow Lantern — Menu Page</title>
<link href="https://fonts.googleapis.com/css2?family=Cormorant+Garamond:wght@400;500&family=Oswald:wght@500&family=Open+Sans:wght@400&display=swap" rel="stylesheet">
<style>
  :root {
    --backdrop: #ffffff;
    --page: #262626;
    --ink: #f2f2f2;
    --ink-soft: #bdbdbd;
    --rule: #9a9a9a;
  }
  * { margin: 0; padding: 0; box-sizing: border-box; }
  html, body { width: 1200px; height: 849px; overflow: hidden; background: var(--backdrop); }
  .canvas { position: relative; width: 1200px; height: 849px; }

  .menu-page {
    position: absolute; left: 291px; top: 24px; width: 618px; height: 800px;
    background: var(--page); color: var(--ink);
    font-family: "Open Sans", sans-serif;
  }

  .masthead { position: absolute; top: 62px; left: 0; right: 0; text-align: center; }
  .masthead-name {
    font-family: "Cormorant Garamond", serif; font-weight: 500;
    font-size: 30px; letter-spacing: 1px; line-height: 1;
  }
  .masthead-tag {
    display: flex; align-items: center; justify-content: center; gap: 10px;
    margin-top: 8px; font-size: 6.5px; letter-spacing: 3.5px; text-transform: uppercase;
  }
  .masthead-tag::before, .masthead-tag::after {
    content: ""; width: 30px; height: 1px; background: var(--ink);
  }

  .section-label {
    position: absolute; display: flex; align-items: center; gap: 10px;
    writing-mode: vertical-rl; transform: rotate(180deg);
    font-family: "Cormorant Garamond", serif; font-weight: 400;
    letter-spacing: 2px; text-transform: uppercase; white-space: nowrap; line-height: 1;
  }
  .section-label::before { content: ""; inline-size: var(--rule-length); block-size: 1px; background: var(--ink); }
  .appetizers-label { left: 40px; top: 176px; font-size: 16px; --rule-length: 90px; }
  .flatbreads-label { left: 96px; top: 448px; font-size: 14px; --rule-length: 40px; }
  .section-note {
    position: absolute; left: 116px; top: 460px;
    writing-mode: vertical-rl; transform: rotate(180deg);
    font-size: 5px; color: var(--ink-soft); white-space: nowrap; letter-spacing: .3px;
  }

  .dish-list { position: absolute; list-style: none; }
  .dish { position: relative; margin-bottom: 9px; }
  .dish-name {
    font-family: "Oswald", sans-serif; font-weight: 500; font-size: 10px;
    text-transform: uppercase; letter-spacing: .3px; line-height: 1.2;
  }
  .dish-desc { font-size: 6px; line-height: 8px; color: var(--ink-soft); }
  .dish-price {
    position: absolute; right: 0; bottom: 0; font-size: 6.5px; line-height: 8px;
    color: var(--ink-soft); text-align: right;
  }
  .dish-ticks { position: absolute; left: -20px; top: 1px; }

  .appetizers-left { left: 84px; top: 180px; width: 180px; }
  .appetizers-right { left: 330px; top: 172px; width: 210px; }
  .flatbreads { left: 156px; top: 452px; width: 170px; }
  .flatbreads .dish { margin-bottom: 14px; }

  .section-divider {
    position: absolute; left: 84px; top: 424px; width: 436px; height: 1px; background: var(--rule);
  }
  .advisory {
    position: absolute; left: 40px; right: 40px; bottom: 26px; text-align: center;
    font-size: 6px; color: var(--ink-soft); letter-spacing: .3px;
  }
</style>
</head>
<body>
<div class="canvas">
  <section class="menu-page">
    <header class="masthead">
      <h1 class="masthead-name">THE WILLOW LANTERN</h1>
      <p class="masthead-tag">Supper Club &amp; Restaurant</p>
    </header>

    <h2 class="section-label appetizers-label">Appetizers</h2>

    <ul class="dish-list appetizers-left">
      <li class="dish">
        <svg class="dish-ticks" width="14" height="10"><g stroke="#f2f2f2" stroke-width="1"><line x1="6" y1="1" x2="14" y2="1"/><line x1="3" y1="5" x2="14" y2="5"/><line x1="0" y1="9" x2="14" y2="9"/></g></svg>
        <p class="dish-name">Soup du Jour</p>
        <p class="dish-desc">Housemade Daily<br>Cup<br>Bowl</p>
        <p class="dish-price">6<br>9</p>
      </li>
      <li class="dish"><p class="dish-name">Fried Coconut Shrimp</p><p class="dish-desc">Mango Lime Coulis</p><p class="dish-price">11</p></li>
      <li class="dish"><p class="dish-name">Crab &amp; Corn Dip</p><p class="dish-desc">Local Lump Crab, Spinach,<br>Cream Cheese, House Fried Tortillas</p><p class="dish-price">13</p></li>
      <li class="dish"><p class="dish-name">The Lantern Bleu<br>Cheese Mussels</p><p class="dish-desc">White Wine, Garlic, Tomatoes,<br>Chorizo Sausage</p><p class="dish-price">14</p></li>
      <li class="dish"><p class="dish-name">Chicken Ginger Spring Rolls</p><p class="dish-desc">With a Spicy Soy Dipping Sauce</p><p class="dish-price">11</p></li>
      <li class="dish"><p class="dish-name">Calamari Our Way</p><p class="dish-desc">Fresh Fried with Herbed Olive Oil,<br>Smoked Paprika Aioli,<br>Parmesan Cheese</p><p class="dish-price">12</p></li>
    </ul>

    <ul class="dish-list appetizers-right">
      <li class="dish"><p class="dish-name">The Lantern Nachos</p><p class="dish-desc">Housemade Chips, Cheese,<br>Jalapeños, Charred Vegetable Salsa,<br>Sour Cream, Shredded Lettuce,<br>Diced Tomatoes Guacamole $2 extra<br>Small<br>Regular</p><p class="dish-price" style="right:40px;">9<br>12</p></li>
      <li class="dish"><p class="dish-name">Shrimp Cocktail</p><p class="dish-desc">Classic Cocktail Sauce</p><p class="dish-price" style="bottom:4px;">4 each</p></li>
      <li class="dish"><p class="dish-name">Oysters on the Half Shell</p><p class="dish-desc">Mignonette, Cocktail Sauce</p><p class="dish-price" style="bottom:4px;">Market Price</p></li>
      <li class="dish"><p class="dish-name">Chilled Lobster Tail</p><p class="dish-desc">Fresh Local Lobster</p><p class="dish-price" style="right:40px;">15</p></li>
      <li class="dish"><p class="dish-name">Ahi Tuna Wontons</p><p class="dish-desc">Tuna Tartare, Spicy Soy, Scallions,<br>Diced Peppers, Wasabi Coulis,<br>Wakame Seaweed, Micro Greens</p><p class="dish-price">Market Price</p></li>
    </ul>

    <div class="section-divider"></div>

    <h2 class="section-label flatbreads-label">Housemade Flatbreads</h2>
    <p class="section-note">All of our flatbreads are baked to order on thin crust</p>

    <ul class="dish-list flatbreads">
      <li class="dish">
        <svg class="dish-ticks" width="14" height="10"><g stroke="#f2f2f2" stroke-width="1"><line x1="6" y1="1" x2="14" y2="1"/><line x1="3" y1="5" x2="14" y2="5"/><line x1="0" y1="9" x2="14" y2="9"/></g></svg>
        <p class="dish-name">BBQ Chicken</p><p class="dish-desc">Grilled Red Onions, Smoked Mozzarella,<br>BBQ Sauce</p><p class="dish-price">14</p>
      </li>
      <li class="dish"><p class="dish-name">The Greek</p><p class="dish-desc">Sliced Tomatoes, Artichoke Hearts,<br>Capers, Fresh Oregano,<br>Banana Peppers, Feta</p><p class="dish-price">15</p></li>
      <li class="dish"><p class="dish-name">The Sausage</p><p class="dish-desc">Sweet Italian, Andouille, Chorizo,<br>Fire Roasted Vegetable Sauce,<br>Grilled Peppers, Wild Mushrooms,<br>Mozzarella, Feta</p><p class="dish-price">15</p></li>
      <li class="dish"><p class="dish-name">Seasonal Selection</p><p class="dish-desc">Chef's Preference, Ask Your Server</p><p class="dish-price">15</p></li>
      <li class="dish"><p class="dish-name">Margarita</p><p class="dish-desc">Fresh Tomatoes, Fresh Mozzarella,<br>Basil, Marinara</p><p class="dish-price">12</p></li>
    </ul>

    <p class="advisory">Consuming Raw or Undercooked Meats, Poultry, Seafood, Shellfish or Egg may Increase Your Risk of Food Borne Illness</p>
  </section>
</div>
</body>
</html>
```